"Willowbrook Circle" Coaching Website Needs a Wordpress Design

"Willowbrook Circle' is a Coaching Website that helps mothers find happiness, freedom, and connection in motherhood.

My website is www.WillowbrookCircle.com

I made the website myself and now would like to get this website professionally designed. I would also like the winner to code the designs and MIGRATE THESE FILES to my Wordpress website. I would like to get designs for ALL 7 PAGES. Due to the 7 pages and the migrating work, I chose the $699 package.

I am including files for the logo and all the pictures and drawings of the website. I am also including some other "women experiencing freedom" pictures to give the kind of "freedom" feel I would like. I will get a new profile picture done after I have my design.

The Feel of my Website:
My motto is that I help mothers "BREAK THE MOM MOULD" to find HAPPINESS, FREEDOM, and CONNECTION in motherhood.
I help mothers be happier by helping them FREE themselves from the societal constraints of motherhood and I help them CONNECT better with other mothers. I have, therefore, attempted to portray Freedom, Connection, and Happiness as emotional benefits.

I made my own logo that corresponds to my videos.

The Rainbow-Freedom picture at the top does not have to stay. I just put it there as an example.

Regarding the Colour:
I have made my own whiteboard videos and corresponding logo and drawings throughout. I used red, blue, green, (and a little bit of purple, yellow, and brown) in my videos due to the fact that they are whiteboard videos. I am having trouble deciding which colours to use for my website in general considering that I have already used these colours in my videos, and drawings. I am not visual and I have NO talent in design. I would love to get YOUR input in what colours to use and everything else design-wise.

My only Design Requirement:
My main requirement is that the header part not take too much space. I want people to immediately see the videos and other content right when they land on the page. I don't want them to have to scroll down.

Thank you so much!! :-)

Target Market(s)

I target DEPRESSED, ANXIOUS, and UNHAPPY mothers, and I help them find HAPPINESS, FREEDOM, and CONNECTION in motherhood.

Industry/Entity Type

Life Coaching

Coding

Coded - Design and coding required

Number of Pages Required

5+ page

Requirements
Must have
• - Please look at my website at www.WillowbrookCircle.com
• - I would like these 7 pages designed.
• - I would like the coded files to be migrated to my website
• - My main requirement is that the header part not take too much space. I want people to immediately see the videos and other content right when they land on the page. I don't want them to have to scroll down.
Nice to have
• - I would ideally like the website to portray the emotional benefits of FREEDOM and CONNECTION. My motto is that I help mothers BREAK THE MOM MOULD to find HAPPINESS, FREEDOM, and CONNECTION in motherhood. I showed this in the logo that I made. :-)
• - The Rainbow-Freedom picture at the top does NOT have to stay if you would prefer to do something else.

```html
<!DOCTYPE html>
<html lang="en">
<head>
<meta charset="utf-8">
<title>Willowbrook Circle – Break the Mom Mould</title>
<link rel="stylesheet" href="https://fonts.googleapis.com/css2?family=Kalam:wght@400;700&family=Lato:wght@400;700;900&display=swap">
<style>
:root{
  --blue:#1b55c6;
  --coral:#f0513f;
  --pink:#e8265e;
  --teal:#17b59b;
  --ink:#222222;
  --body:#3a3a3a;
  --grey-band:#efefef;
  --line:#d6d6d6;
  --white:#ffffff;
  --hero-mid:#5a6068;
}
*{box-sizing:border-box;margin:0;padding:0}
html,body{width:1200px;height:3169px;overflow:hidden;background:var(--white)}
body{position:relative;font-family:'Lato',sans-serif;color:var(--body)}
.abs{position:absolute}

/* header */
.site-header{top:0;left:0;width:1200px;height:190px}
.doodle{background:#f3ecef;border-radius:8px}
.contact-line{font-size:15px;color:var(--ink)}
.brand{left:400px;top:20px;width:400px;height:80px;display:flex;align-items:center;justify-content:center;gap:14px}
.brand-dot{width:26px;height:26px;border-radius:50%;background:var(--teal)}
.brand-name{font-family:'Kalam',cursive;font-weight:700;font-size:40px;color:var(--blue);line-height:1}
.main-nav{top:127px;left:99px;width:1002px;height:52px;border-top:2px solid #9a9a9a;border-bottom:2px solid #9a9a9a}
.main-nav a{position:absolute;top:14px;font-size:13px;font-weight:700;color:var(--ink);text-decoration:none;letter-spacing:.3px}
.main-nav a.active{color:var(--teal)}

/* hero */
.hero{top:190px;left:0;width:1200px;height:575px;overflow:hidden}
.hero-bg{position:absolute;inset:0;background:
  radial-gradient(ellipse 520px 360px at 880px 300px,rgba(240,200,120,.35),transparent 70%),
  radial-gradient(ellipse 700px 420px at 1000px 560px,rgba(120,170,140,.35),transparent 70%),
  linear-gradient(180deg,#3a3f46 0%,var(--hero-mid) 45%,#4a4a44 100%)}
.hero-text{font-family:'Kalam',cursive;font-size:21px;line-height:1.35;color:var(--white)}
.hero-lead{left:99px;top:48px;width:500px}
.video{left:99px;top:118px;width:459px;height:313px;background:var(--white)}
.video-art{position:absolute;left:0;top:0;width:459px;height:270px;background:linear-gradient(135deg,#f6f4f4,#e9e6ee)}
.video-bar{position:absolute;left:0;bottom:0;width:459px;height:43px;background:#111}
.hero-sub{left:99px;top:446px;width:450px}
.hero-cta-text{left:690px;top:322px;width:412px;text-align:right;font-size:22px;line-height:1.38}
.hero-btns{left:672px;top:452px;height:49px;display:flex}
.btn-grey{width:272px;background:#d9d9d9;color:var(--ink);font-weight:700;font-size:17px;display:flex;align-items:center;justify-content:center;border-radius:5px 0 0 5px;letter-spacing:.4px}
.btn-pink{width:157px;background:var(--pink);color:var(--white);font-weight:700;font-size:17px;display:flex;align-items:center;justify-content:center;border-radius:0 5px 5px 0;letter-spacing:.4px}

/* shared */
.sec-title{font-weight:900;font-size:35px;color:var(--blue);letter-spacing:.3px}
.sec-title span{color:var(--coral)}
.btn-coral{display:flex;align-items:center;justify-content:center;background:var(--coral);color:var(--white);font-size:15px;letter-spacing:.5px;border:2px solid #c93a2a;box-shadow:2px 2px 0 #c93a2a;font-family:'Kalam',cursive}
.copy{font-size:14.5px;line-height:1.6;color:var(--body)}

/* about */
.about-title{left:99px;top:800px}
.about-rule{left:99px;top:852px;width:330px;height:2px;background:var(--blue)}
.about-copy{left:99px;top:884px;width:650px}
.about-copy p+p{margin-top:18px}
.about-btn{left:99px;top:1082px;width:123px;height:36px}
.portrait{left:784px;top:849px;width:317px;height:260px;border:2px dashed #bbb;padding:10px;background:var(--white)}
.portrait div{width:100%;height:100%;background:linear-gradient(160deg,#a7b8c6,#c98a5c 60%,#5b6069)}

/* cheat sheet */
.optin{top:1179px;left:0;width:1200px;height:307px;background:var(--grey-band)}
.optin-art{left:101px;top:36px;width:353px;height:243px;background:linear-gradient(135deg,#f6f6f6,#e3ecee);border-radius:6px}
.optin-title{left:539px;top:50px;width:562px;font-family:'Kalam',cursive;font-weight:700;font-size:19px;color:var(--blue);white-space:nowrap}
.optin-title span{color:var(--coral)}
.optin-rule{left:539px;top:90px;width:560px;height:2px;background:#666}
.optin-sub{left:539px;top:117px;font-family:'Kalam',cursive;font-size:15px;color:var(--ink)}
.optin-input{left:539px;top:163px;width:349px;height:31px;border:1px solid var(--line);background:var(--white);font-size:12px;color:#999;padding:7px 10px}
.optin-icons{left:919px;top:152px;width:176px;height:50px;background:linear-gradient(90deg,#e4eef8,#e4f4ec);border-radius:4px}
.optin-btn{left:539px;top:220px;width:232px;height:34px}

/* products */
.prod-title{top:1518px;left:0;width:1200px;text-align:center;font-size:27px}
.prod-rule{left:476px;top:1562px;width:250px;height:2px;background:var(--ink)}
.art{background:linear-gradient(135deg,#f7f7f7,#e8eef2);border-radius:6px}
.num{width:43px;height:43px;border:2px solid var(--coral);border-radius:50%;color:var(--coral);font-family:'Kalam',cursive;font-size:20px;display:flex;align-items:center;justify-content:center}
.item-title{font-family:'Kalam',cursive;font-weight:700;font-size:17px;line-height:1.45;color:var(--ink);text-transform:uppercase}
.item-copy{font-size:13.5px;line-height:1.65}
.more{color:var(--coral)}

/* blog */
.blog{top:2489px;left:0;width:1200px;height:380px;background:var(--grey-band)}
.blog-title{top:34px;left:0;width:1200px;text-align:center;font-size:27px}
.blog-rule{left:476px;top:80px;width:250px;height:2px;background:var(--ink)}
.card{top:131px;width:486px;height:186px;background:var(--white)}
.card-art{position:absolute;left:0;top:0;width:198px;height:186px;background:linear-gradient(135deg,#f4f4f4,#e2e6ef)}
.card-body{position:absolute;left:212px;top:12px;width:262px}
.card-title{font-family:'Kalam',cursive;font-size:15px;line-height:1.35;color:var(--coral)}
.card-text{font-size:12px;line-height:1.6;margin-top:6px}
.card-more{font-size:12px;color:var(--coral);text-decoration:underline;margin-top:6px;display:block}
.arrow{top:208px;width:24px;height:30px}

/* footer */
.foot-nav{top:2912px;left:0;width:1200px;height:24px}
.foot-nav a{position:absolute;top:0;font-size:13px;font-weight:700;color:var(--ink);text-decoration:none}
.foot-rule{left:99px;top:2960px;width:1002px;height:1px;background:var(--line)}
.foot-input{left:99px;top:2996px;width:197px;height:38px;border:1px solid #999;font-size:12px;color:#999;padding:10px}
.foot-btn{left:298px;top:2996px;width:110px;height:38px;background:var(--coral);color:var(--white);font-size:13px;font-weight:700;display:flex;align-items:center;justify-content:center;border:2px solid #c93a2a}
.social{left:923px;top:2996px;display:flex;gap:6px}
.social span{width:31px;height:31px;border-radius:4px;display:block}
.foot-deco{left:0;top:3064px;width:1200px;height:54px;background:linear-gradient(180deg,#fafafa,#f1f1f1)}
.copyright{left:0;top:3121px;width:1200px;height:48px;background:var(--teal);color:var(--white);font-size:13px;display:flex;align-items:center;justify-content:center}
</style>
</head>
<body>

<header class="abs site-header">
  <div class="abs doodle" style="left:99px;top:20px;width:64px;height:72px" role="img" aria-label="Hand-drawn stick figure mother with a phone bubble"></div>
  <div class="abs contact-line" style="left:163px;top:62px">(555) 201-3380 (USA)</div>
  <div class="abs brand">
    <span class="brand-dot"></span>
    <span class="brand-name">Willowbrook Circle</span>
  </div>
  <div class="abs contact-line" style="left:830px;top:62px">delia@willowbrookcircle.com</div>
  <div class="abs doodle" style="left:1034px;top:20px;width:67px;height:72px" role="img" aria-label="Hand-drawn stick figure mother with an envelope"></div>
  <nav class="abs main-nav">
    <a class="active" style="left:13px">HOME</a>
    <a style="left:112px">ABOUT ME</a>
    <a style="left:260px">BREAK THE MOM MOULD!</a>
    <a style="left:512px">FAQs</a>
    <a style="left:611px">PRODUCTS/SERVICES</a>
    <a style="left:816px">CONTACT ME</a>
    <a style="left:958px">BLOG</a>
  </nav>
</header>

<section class="abs hero">
  <div class="hero-bg" role="img" aria-label="Silhouette of a woman with raised arms in front of a rainbow sky"></div>
  <p class="abs hero-text hero-lead">Have You been Suffering from DEPRESSION, ANXIETY, or EMOTIONAL DISTRESS in Motherhood?</p>
  <div class="abs video">
    <div class="video-art" role="img" aria-label="Whiteboard video still: a stack of books, a television and a stick figure mother"></div>
    <svg class="abs" style="left:200px;top:100px" width="60" height="60" viewBox="0 0 60 60"><circle cx="30" cy="30" r="28" fill="#e8265e"/><path d="M24 18 L42 30 L24 42Z" fill="#fff"/></svg>
    <div class="video-bar">
      <svg class="abs" style="left:14px;top:11px" width="40" height="22" viewBox="0 0 40 22"><rect x="0" y="2" width="5" height="18" fill="#fff"/><rect x="9" y="2" width="5" height="18" fill="#fff"/><path d="M22 2 L38 11 L22 20Z" fill="#fff"/></svg>
      <div class="abs" style="left:70px;top:19px;width:370px;height:5px;background:#555"></div>
      <div class="abs" style="left:70px;top:19px;width:110px;height:5px;background:#e8265e"></div>
    </div>
  </div>
  <p class="abs hero-text hero-sub">To DISCOVER THE REAL CAUSE OF THESE EMOTIONS, and How YOU can ESCAPE them!</p>
  <p class="abs hero-text hero-cta-text">To Find Out More about How I can PERSONALLY Help You BREAK the Mom Mould, CLICK HERE:</p>
  <div class="abs hero-btns">
    <span class="btn-grey">THE COACHING PROGRAM</span>
    <span class="btn-pink">GET STARTED</span>
  </div>
</section>

<section>
  <h2 class="abs sec-title about-title">ABOUT <span>DELIA HARTWELL</span></h2>
  <div class="abs about-rule"></div>
  <div class="abs copy about-copy">
    <p>Delia Hartwell is a Certified Professional Coach who helps mothers be happier in motherhood by helping them escape from the harmful aspects of our mothering culture. She is also the mother of three children ranging from 2 to 7 years old.</p>
    <p>Delia grew up in Halifax, Nova Scotia. She originally got an Arts degree in Anthropology due to her fascination with distant places and cultures. She lived in 7 foreign countries in her twenties (Portugal, Spain, Denmark, Norway, Austria, Italy, and Greece), where she lived with the locals and learned their languages.</p>
  </div>
  <span class="abs btn-coral about-btn">READ MORE</span>
  <div class="abs portrait"><div role="img" aria-label="Portrait photo of the coach outdoors by a river"></div></div>
</section>

<section class="abs optin">
  <div class="abs optin-art" role="img" aria-label="Drawing of two stick figure mothers beside a free cheat sheet"></div>
  <h3 class="abs optin-title">Enter Your Email Address to Receive Your <span>FREE CHEET SHEET:</span></h3>
  <div class="abs optin-rule"></div>
  <p class="abs optin-sub">A Copy Of This Video, And A Subscription To My Free Email Course...</p>
  <div class="abs optin-input">Email</div>
  <div class="abs optin-icons" role="img" aria-label="Small drawings of a cheat sheet, a video and an email course"></div>
  <span class="abs btn-coral optin-btn">FREE CHEAT SHEET</span>
</section>

<section>
  <h2 class="abs sec-title prod-title">PRODUCTS <span>&amp; SERVICES</span></h2>
  <div class="abs prod-rule"></div>

  <div class="abs art" style="left:137px;top:1560px;width:307px;height:232px" role="img" aria-label="Drawing of two stick figure mothers holding a laptop showing a free email course"></div>
  <div class="abs num" style="left:570px;top:1617px">1</div>
  <h3 class="abs item-title" style="left:619px;top:1622px;width:480px">FREE "BREAK THE MOM MOULD" EMAIL COURSE</h3>
  <p class="abs copy item-copy" style="left:619px;top:1672px;width:470px">I currently offer a Free Email Course with articles, audios, and videos that help you ESCAPE from the harmful beliefs and expectations of our Mothering Culture to find HAPPINESS in motherhood.</p>
  <span class="abs btn-coral" style="left:619px;top:1794px;width:205px;height:36px">FREE EMAIL COURSE</span>

  <div class="abs num" style="left:144px;top:1912px">2</div>
  <h3 class="abs item-title" style="left:201px;top:1917px;width:470px">6-TO-12 WEEK "BREAK THE MOM MOULD" COACHING PROGRAM</h3>
  <p class="abs copy item-copy" style="left:201px;top:1990px;width:475px">In this unique program, I help mothers be HAPPIER in motherhood by helping them ESCAPE from what I call "THE MOM MOULD". The Mom Mould is all the cultural beliefs, rules, and expectations that force mothers to feel painful emotions like guilt, fear, shame, failure, disappointment, powerlessness, loneliness, depression, anxiety, anger, rage, and resentment <span class="more">...[+]</span></p>
  <span class="abs btn-coral" style="left:201px;top:2126px;width:253px;height:36px">THE COACHING PROGRAM</span>
  <div class="abs art" style="left:714px;top:1912px;width:385px;height:169px" role="img" aria-label="Drawing of the Mom Mould box filled with painful emotion words beside a stick figure mother"></div>

  <div class="abs art" style="left:106px;top:2244px;width:359px;height:203px" role="img" aria-label="Drawing of stick figure mothers standing outside the Mom Mould box"></div>
  <div class="abs num" style="left:570px;top:2250px">3</div>
  <h3 class="abs item-title" style="left:619px;top:2258px;width:480px">GRADUATE COACHING - BEYOND THE MOM MOULD!</h3>
  <p class="abs copy item-copy" style="left:619px;top:2300px;width:475px">For any mothers who would like to continue working with me after they have broken free of the Mom Mould, I offer Graduate Coaching on a weekly, biweekly, monthly, or casual basis ...<span class="more">[+]</span></p>
  <span class="abs btn-coral" style="left:619px;top:2392px;width:251px;height:38px">BEYOND THE MOM MOULD</span>
</section>

<section class="abs blog">
  <h2 class="abs sec-title blog-title">HAPPINESS <span>BLOG</span></h2>
  <div class="abs blog-rule"></div>
  <svg class="abs arrow" style="left:47px" viewBox="0 0 24 30"><path d="M18 3 L6 15 L18 27" fill="none" stroke="#bbb" stroke-width="2"/></svg>
  <article class="abs card" style="left:99px">
    <div class="card-art" role="img" aria-label="Drawing of a preacher at a podium"></div>
    <div class="card-body">
      <h4 class="card-title">"ENJOY YOUR BABY!" and other Ridiculous Preachings</h4>
      <p class="card-text">I have an interesting experiment that I invite you to participate in. Close your eyes, and imagine spending time with a really good friend of yours.</p>
      <a class="card-more">Read More</a>
    </div>
  </article>
  <article class="abs card" style="left:625px">
    <div class="card-art" role="img" aria-label="Drawing of a psychologist seated in an armchair"></div>
    <div class="card-body">
      <h4 class="card-title">Embracing that future psychologist's couch!</h4>
      <p class="card-text">There is an expectation in our society that mothers must ensure that their children be happy at all times. We are seen as psychologists who must be</p>
      <a class="card-more">Read More</a>
    </div>
  </article>
  <svg class="abs arrow" style="left:1125px" viewBox="0 0 24 30"><path d="M6 3 L18 15 L6 27" fill="none" stroke="#bbb" stroke-width="2"/></svg>
</section>

<footer>
  <nav class="abs foot-nav">
    <a style="left:101px">HOME</a>
    <a style="left:205px">ABOUT ME</a>
    <a style="left:355px">BREAK THE MOM MOULD!</a>
    <a style="left:611px">FAQs</a>
    <a style="left:710px">PRODUCTS/SERVICES</a>
    <a style="left:915px">CONTACT ME</a>
    <a style="left:1065px">BLOG</a>
  </nav>
  <div class="abs foot-rule"></div>
  <div class="abs foot-input">Enter your email here</div>
  <span class="abs foot-btn">SUBSCRIBE</span>
  <div class="abs social">
    <span style="background:var(--blue)"></span>
    <span style="background:#5aa9e6"></span>
    <span style="background:var(--coral)"></span>
    <span style="background:#2a7ab8"></span>
    <span style="background:var(--pink)"></span>
  </div>
  <div class="abs foot-deco" role="img" aria-label="Faint row of hand-drawn stick figure mothers"></div>
  <div class="abs copyright">Copyright ©&nbsp;2017&nbsp;<strong>Willowbrook Circle</strong>.&nbsp;All Rights Reserved.</div>
</footer>

</body>
</html>
```